Lanternfield Disability - Social Security Disability Attorneys

Our company is expanding to attract clients nationwide for our social security disability practice. We have a logo, but I am looking for a creative and elegant letterhead that projects an image of being technologically advanced but still professional enough for the legal field. I am looking for the "wow factor" combined with this is still professional enough for a law practice.

Requesting letterhead and business card design
Updates

Had to update and change the logo. The previous logo had a typo. Please send updates with the new logo for consideration. The letterhead and business cards should be professional enough to be used for a law firm. Thanks.

Industry/Entity Type

Law Practice, Law Firm, Healthcare Industry, Government

Colors

Designer to choose colors to be used in the design.

Requirements
Nice to have
• **Please create a vertical design for the business card**

```html
<!DOCTYPE html>
<html lang="en">
<head>
<meta charset="utf-8">
<title>Lanternfield Disability – Letterhead</title>
<link rel="stylesheet" href="https://fonts.googleapis.com/css2?family=Tinos:wght@400&family=Montserrat:wght@500&family=Roboto+Condensed:wght@400;700&display=swap">
<style>
  :root{
    --backdrop:#2a2b2d;
    --paper:#ffffff;
    --ink:#1c1c1c;
    --brand-blue:#1f5fa8;
    --tag-grey:#555a60;
    --rule-grey:#b9bcc0;
    --wash-grey:#eceef1;
    --sign-blue:#c9d2e6;
  }
  *{box-sizing:border-box;margin:0;padding:0}
  html,body{width:1200px;height:900px;overflow:hidden;background:var(--backdrop)}
  .letterhead{
    position:absolute;left:260px;top:10px;width:680px;height:880px;
    background:var(--paper);
    font-family:"Tinos","Times New Roman",serif;color:var(--ink);
    overflow:hidden;
  }
  .brand{position:absolute;top:52px;right:52px;display:flex;align-items:center}
  .brand-name{
    font-family:"Tinos","Times New Roman",serif;font-size:22px;
    color:var(--brand-blue);text-transform:uppercase;letter-spacing:.5px;
    margin-right:14px;margin-top:22px;
  }
  .brand-tagline{
    border-left:1px solid var(--rule-grey);padding:4px 0 4px 9px;
    font-family:"Montserrat",Arial,sans-serif;font-weight:500;
    font-size:7.5px;letter-spacing:2px;text-transform:uppercase;
    color:var(--tag-grey);line-height:15px;
  }
  .recipient{position:absolute;top:215px;left:98px;display:flex;font-size:13px;line-height:16px}
  .recipient-label{width:44px}
  .salutation{position:absolute;top:318px;left:88px;font-size:13px}
  .body{position:absolute;top:348px;left:88px;width:550px;font-size:13px;line-height:16px}
  .body p{margin-bottom:16px}
  .closing{position:absolute;top:632px;left:104px;font-size:13px}
  .signature{position:absolute;top:652px;left:108px;width:180px;height:52px}
  .page-wash{position:absolute;left:0;right:0;bottom:0;height:230px;
    background:linear-gradient(to bottom,rgba(236,238,241,0),var(--wash-grey))}
  .contact{
    position:absolute;left:120px;bottom:62px;
    font-family:"Roboto Condensed",Arial,sans-serif;font-size:9.5px;
    line-height:15px;color:var(--ink);text-transform:uppercase;
  }
  .contact b{font-weight:700}
</style>
</head>
<body>
  <main class="letterhead">
    <header class="brand">
      <div class="brand-name">Lanternfield Disability</div>
      <div class="brand-tagline">Social<br>Security<br>Disability<br>Attorneys</div>
    </header>

    <section class="recipient">
      <div class="recipient-label">To:</div>
      <address style="font-style:normal">Mr./Mrs. Customerand Partner<br>240 Maple Row<br>New York<br>NY 10012</address>
    </section>

    <p class="salutation">Dear Customer,</p>

    <section class="body">
      <p>Lorem ipsum dolor sit amet, consetetur sadipscing elitr, sed diam nonumy eirmod tempor invidunt ut labore et dolore magna aliquyam erat, sed diam voluptua. At vero eos et accusam et justo duo dolores et ea rebum. Stet clita kasd gubergren, no sea takimata sanctus est Lorem ipsum dolor sit amet. Lorem ipsum dolor sit amet, consetetur sadipscing elitr, sed diam nonumy eirmod tempor invidunt ut labore et dolore magna aliquyam erat, sed diam voluptua. At vero eos et accusam et justo duo dolores et ea rebum. Stet clita kasd gubergren, no sea takimata sanctus est Lorem ipsum dolor sit amet.</p>
      <p>Duis autem vel eum iriure dolor in hendrerit in vulputate velit esse molestie consequat, vel illum dolore eu feugiat nulla facilisis at vero eros et accumsan et iusto odio dignissim qui blandit praesent luptatum zzril delenit augue duis dolore te feugait nulla facilisi. Lorem ipsum dolor sit amet, consectetuer adipiscing elit, sed diam nonummy nibh euismod tincidunt ut laoreet dolore magna aliquam erat volutpat.</p>
      <p>Nam liber tempor cum soluta nobis eleifend option congue nihil imperdiet doming id quod mazim placerat facer possim assum. Lorem ipsum dolor sit amet, consectetuer adipiscing elit, sed diam nonummy nibh euismod tincidunt ut laoreet dolore magna aliquam erat volutpat. Ut wisi enim ad minim veniam, quis nostrud exerci tation ullamcorper suscipit lobortis nisl ut aliquip ex ea commodo consequat.</p>
    </section>

    <p class="closing">Sincerely,</p>
    <svg class="signature" viewBox="0 0 180 52" role="img" aria-label="Handwritten signature of Daniel Whitcombe">
      <rect x="0" y="8" width="180" height="36" rx="6" fill="var(--sign-blue)"/>
    </svg>

    <div class="page-wash"></div>

    <address class="contact" style="font-style:normal">
      1840 Harrow Ridge<br>Atlanta, GA 30309<br><b>P:</b> 404-555-0142<br><b>F:</b> 404-555-0176
    </address>
  </main>
</body>
</html>
```